Morvell Electric Business Card

An electrical contractor needs a business card design, that will stand out.
I would like designs that use the colors in the logo shown. The logo attached I am ok with but if you have a better idea I am open for suggestions. I like the color scheme.
Industry/Entity Type
Electrical
Contact Information for Business Card
Services, social media, QR code,

```html
<!DOCTYPE html>
<html lang="en">
<head>
<meta charset="utf-8">
<title>Morvell Electric Business Card</title>
<link rel="stylesheet" href="https://fonts.googleapis.com/css2?family=Montserrat:wght@700&family=Overpass:wght@400&display=swap">
<style>
  :root {
    --backdrop: #7b7b7b;
    --card: #262324;
    --accent: #f2b807;
    --light: #ffffff;
  }
  * { margin: 0; padding: 0; box-sizing: border-box; }
  html, body { width: 1133px; height: 1200px; overflow: hidden; }
  body { background: var(--backdrop); position: relative; font-family: "Overpass", sans-serif; }
  .card {
    position: absolute;
    left: 200px;
    width: 730px;
    height: 418px;
    border-radius: 24px;
    background: var(--card);
    overflow: hidden;
  }
  .card--front { top: 139px; }
  .card--back { top: 642px; }
  .accent-panel { position: absolute; left: 0; top: 0; width: 730px; height: 418px; }
  .company-title {
    position: absolute;
    right: 40px;
    top: 56px;
    font-family: "Montserrat", sans-serif;
    font-weight: 700;
    font-size: 32px;
    letter-spacing: 0.2px;
    color: var(--light);
  }
  .person { position: absolute; right: 45px; top: 146px; text-align: right; }
  .person__name {
    font-family: "Montserrat", sans-serif;
    font-weight: 700;
    font-size: 22px;
    letter-spacing: 0.6px;
    color: var(--accent);
    line-height: 26px;
  }
  .person__role { font-size: 16px; color: var(--light); line-height: 20px; letter-spacing: 0.4px; }
  .address {
    position: absolute;
    right: 45px;
    top: 214px;
    text-align: right;
    font-size: 16px;
    line-height: 20px;
    letter-spacing: 0.4px;
    color: var(--light);
  }
  .contacts { position: absolute; right: 46px; top: 274px; list-style: none; }
  .contacts li {
    display: flex;
    justify-content: flex-end;
    align-items: center;
    gap: 10px;
    height: 20.5px;
    font-size: 16px;
    letter-spacing: 0.4px;
    color: var(--light);
  }
  .contacts svg { width: 14px; height: 14px; flex: none; }
  .brand {
    position: absolute;
    left: 0; right: 0;
    top: 120px;
    display: flex;
    flex-direction: column;
    align-items: center;
    gap: 24px;
  }
  .brand__dot { width: 120px; height: 120px; border-radius: 50%; background: var(--accent); }
  .brand__name {
    font-family: "Montserrat", sans-serif;
    font-weight: 700;
    font-size: 38px;
    color: var(--light);
    letter-spacing: 0.2px;
  }
</style>
</head>
<body>
  <section class="card card--front">
    <svg class="accent-panel" viewBox="0 0 730 418" aria-hidden="true">
      <polygon points="0,0 276,0 105,418 0,418" fill="var(--accent)"/>
    </svg>
    <h1 class="company-title">MORVELL ELECTRIC</h1>
    <div class="person">
      <p class="person__name">DANIEL REYES</p>
      <p class="person__role">President</p>
    </div>
    <p class="address">2140 Birchwood Court<br>Fairbanks, Alaska 99701</p>
    <ul class="contacts">
      <li>555-218-4730
        <svg viewBox="0 0 16 16"><path d="M3 1.5l3 .5 1 3.5-2 1.2a9 9 0 0 0 4.3 4.3L10.5 9l3.5 1 .5 3-2 2C6.5 15 1 9.5 1 3.5z" fill="var(--accent)"/></svg>
      </li>
      <li>555-604-1982
        <svg viewBox="0 0 16 16"><rect x="4" y="1" width="8" height="14" rx="1.5" fill="none" stroke="var(--accent)" stroke-width="1.8"/></svg>
      </li>
      <li>555-377-2056
        <svg viewBox="0 0 16 16"><rect x="4" y="2" width="8" height="5" fill="var(--accent)"/><rect x="1" y="7.5" width="14" height="6.5" rx="1" fill="var(--accent)"/></svg>
      </li>
      <li>info@morvellelectric.com
        <svg viewBox="0 0 16 16"><rect x="1" y="3.5" width="14" height="9.5" fill="var(--accent)"/><path d="M1.5 4l6.5 5 6.5-5" fill="none" stroke="var(--card)" stroke-width="1.2"/></svg>
      </li>
      <li>morvellelectric.com
        <svg viewBox="0 0 16 16"><circle cx="8" cy="8" r="7" fill="var(--accent)"/><path d="M5 4.5c2 .5 1 2.5 3 3s1 3-1 4.5M10.5 3.5c-.5 1.5 1 2 2.5 2.5" fill="none" stroke="var(--card)" stroke-width="1.2"/></svg>
      </li>
    </ul>
  </section>

  <section class="card card--back">
    <div class="brand">
      <span class="brand__dot" aria-hidden="true"></span>
      <p class="brand__name">MORVELL ELECTRIC</p>
    </div>
  </section>
</body>
</html>
```